Packaging label for Multi purpose ointment/balm

I would like to change packaging label (design) for multi purpose ointment (balm) that I have. Name of company is Vela Orin and I named the product (ointment) TUSKLEN. I attached pictures of existing label that i have (first file). The other 3 files are just changes that I was thinking to add. I would like to completely change look (design) of label. I was thinking to remove name TUSKLEN and make it more stand out "multi purpose ointment" instead. But word TUSKLEN can also stay on it if you think that would come out better. I was also thinking to change it to balm instead of ointment.
So I would like on label to stand out:
-multi purpose ointment or balm
-skin
-muscles
-joints
Ointment would be mostly use for skin problems, so I was thinking to add something like: cuts, burns, scrapes,... next to the word "skin".
Please feel free to use creation and completely change the look of label (design), because I want completely different design, and not similar design.
Here is description of multi purpose ointment:
Tusklen is multi purpose ointment with pain relief, anti-inflammatory and other healing properties for skin, muscles and joints. It is all natural, non-gmo, and made from the finest plant-based ingredients.
PURPOSE AND USE
Tusklen is a multi purpose ointment suitable for everyday use. It can be used to treat various injuries and phenomena of the skin such as wounds, sores, ulcers, mastitis, insect bites, burns, whitlow, herpes, aphthae, bruises, blisters and fungal infections with healing effects generally visible within 3 days. Do not apply directly on open wounds. It may be covered with a loosely wrapped sterile bandage that does not inhibit blood circulation. Tusklen also reduces swelling and relieves pain caused by rheumatism, gout, sciatica, arthritis. It can also be applied as a massage balm to improve blood circulation, reduce inflammation of muscles and ligaments, and alleviate back pain, joint pain, shoulder pain and other muscle soreness. For best results, massage affected area several times a day. In addition, the ointment can be used to effectively relieve nasal and upper respiratory congestion (apply around the nose, chest and throat). Tusklen may also be applied as a daily moisturizer to revitalize skin and prevent the formation of stretch marks. After use, the skin is soft and toned.
marlow Market(s)
Stores like brightcart, shopvane, marlow, bulkery, stores with natural products,...
Industry/Entity Type
It Company
Font styles to use
Requirements
Nice to have
- I want completely different design. Not similar design.

```html
<!DOCTYPE html>
<html lang="en">
<head>
<meta charset="utf-8">
<title>Vela Orin – Multi Purpose Ointment Labels</title>
<link href="https://fonts.googleapis.com/css2?family=Comfortaa:wght@400&family=Montserrat:wght@700;800&display=swap" rel="stylesheet">
<style>
  :root {
    --teal: #2eb5a4;
    --teal-text: #22a898;
    --white: #ffffff;
    --backdrop: #d9d9d9;
  }
  * { box-sizing: border-box; margin: 0; padding: 0; }
  html, body { width: 1200px; height: 686px; overflow: hidden; }
  body { background: var(--backdrop); position: relative; }

  .label {
    position: absolute;
    top: 300px;
    width: 290px;
    height: 220px;
    background: var(--white);
    overflow: hidden;
  }
  .label--skin { left: 80px; }
  .label--joints { left: 455px; }
  .label--muscles { left: 830px; }

  .brand-name {
    font-family: "Comfortaa", sans-serif;
    font-weight: 400;
    color: var(--white);
    position: absolute;
    white-space: nowrap;
    line-height: 1;
  }
  .product-type {
    font-family: "Montserrat", sans-serif;
    font-weight: 800;
    font-size: 23px;
    line-height: 27px;
    letter-spacing: 0.5px;
    position: absolute;
    white-space: nowrap;
  }
  .use-area {
    font-family: "Montserrat", sans-serif;
    font-weight: 800;
    position: absolute;
    writing-mode: vertical-rl;
    transform: rotate(180deg);
    letter-spacing: 1px;
    line-height: 1;
  }
  .divider { position: absolute; width: 2px; }

  /* SKIN label */
  .label--skin .top-band {
    position: absolute; left: 0; top: 0; width: 100%; height: 100px;
    background: var(--teal);
  }
  .label--skin .frame {
    position: absolute; left: 24px; top: 20px; width: 238px; height: 186px;
    border: 2px solid;
    border-image: linear-gradient(var(--white) 0 43%, var(--teal) 43% 100%) 1;
  }
  .label--skin .brand-name { left: 36px; top: 56px; font-size: 38px; }
  .label--skin .product-type { left: 38px; top: 110px; color: var(--teal-text); }
  .label--skin .divider { left: 220px; top: 112px; height: 82px; background: var(--teal); }
  .label--skin .use-area { left: 228px; top: 112px; height: 84px; font-size: 26px; color: var(--teal-text); text-align: center; }

  /* JOINTS label */
  .label--joints .panel {
    position: absolute; left: 20px; top: 18px; width: 250px; height: 186px;
    background: var(--teal);
  }
  .label--joints .brand-name { left: 34px; top: 34px; font-size: 38px; }
  .label--joints .name-rule { position: absolute; left: 34px; top: 80px; width: 218px; height: 2px; background: var(--white); }
  .label--joints .product-type { left: 34px; top: 98px; color: var(--white); line-height: 32px; }
  .label--joints .divider { left: 212px; top: 96px; height: 98px; background: var(--white); }
  .label--joints .use-area { left: 222px; top: 96px; height: 100px; font-size: 24px; color: var(--white); text-align: center; }

  /* MUSCLES label */
  .label--muscles .name-block {
    position: absolute; left: 58px; top: 16px; width: 132px; height: 86px;
    background: var(--teal);
  }
  .label--muscles .brand-name { left: 70px; top: 24px; font-size: 33px; line-height: 33px; }
  .label--muscles .product-type { left: 60px; top: 120px; color: var(--teal-text); line-height: 26px; }
  .label--muscles .use-area { left: 238px; top: 20px; height: 160px; font-size: 25px; color: var(--teal-text); text-align: right; }
</style>
</head>
<body>

  <section class="label label--skin">
    <div class="top-band"></div>
    <div class="frame"></div>
    <div class="brand-name">Vela Orin</div>
    <div class="product-type">MULTI<br>PURPOSE<br>OINTMENT</div>
    <div class="divider"></div>
    <div class="use-area">SKIN</div>
  </section>

  <section class="label label--joints">
    <div class="panel"></div>
    <div class="brand-name">Vela Orin</div>
    <div class="name-rule"></div>
    <div class="product-type">MULTI<br>PURPOSE<br>OINTMENT</div>
    <div class="divider"></div>
    <div class="use-area">JOINTS</div>
  </section>

  <section class="label label--muscles">
    <div class="name-block"></div>
    <div class="brand-name">Vela<br>Orin</div>
    <div class="product-type">MULTI<br>PURPOSE<br>OINTMENT</div>
    <div class="use-area">MUSCLES</div>
  </section>

</body>
</html>
```